Flyer Design für Berater
Zielgruppe
Beratung für kleinere Unternehmen (z.B. KMUs, Stiftungen, Verbände)
intern bei Grossunternehmen
Aufgabenstellung
Schlichtes Design, Fraben türkis - blau
zu 70% als digitales pdf zu verwenden, zu 30 % als print

```html
<!DOCTYPE html>
<html lang="de">
<head>
<meta charset="utf-8">
<title>Flyer Beratung</title>
<link href="https://fonts.googleapis.com/css2?family=Fira+Sans:wght@400;500;600&family=PT+Sans:wght@400;700&display=swap" rel="stylesheet">
<style>
:root{
  --blue:#2e5a94;
  --blue-dark:#244c82;
  --ink:#3a3a3a;
  --grey-box:#dedede;
  --line:#c8c8c8;
  --olive:#c9c46a;
  --coral:#e26b55;
  --sky:#b9cbd8;
  --leaf:#5c6a2e;
}
*{margin:0;padding:0;box-sizing:border-box}
html,body{width:926px;height:1200px;overflow:hidden;background:#fff}
body{position:relative;font-family:"PT Sans",sans-serif;color:var(--ink)}
.page{position:absolute;width:334px;height:472px;background:#fff;border:1px solid var(--line);overflow:hidden}
.page-cover{left:114px;top:88px}
.page-dynamics{left:468px;top:88px}
.page-development{left:114px;top:644px}
.page-profile{left:467px;top:644px}
.abs{position:absolute}
.brand{position:absolute;right:7px;top:6px;display:flex;align-items:flex-start;gap:3px}
.brand-address{font-size:3.4px;line-height:4.6px;text-align:right;color:var(--blue-dark);font-weight:700;padding-top:2px}
.brand-mark{width:25px;height:25px;background:#f2f2f2;border:1px solid #d8d8d8;display:flex;align-items:flex-end;justify-content:center;font-family:"Fira Sans",sans-serif;font-weight:600;font-size:10px;color:var(--blue);padding-bottom:1px}
h2.title{font-family:"Fira Sans",sans-serif;font-weight:500;color:var(--blue);font-size:13.5px;line-height:16px}
h3.sub{font-family:"Fira Sans",sans-serif;font-weight:500;color:var(--blue);font-size:8.6px}
.label{font-family:"Fira Sans",sans-serif;font-weight:600;color:var(--blue);font-size:6.4px}
p,li{font-size:6px;line-height:8.1px}
p+p{margin-top:8px}
.grey-box{background:var(--grey-box);padding:5px 6px 4px 20px}
.grey-box ul{list-style:none}
.grey-box li{position:relative}
.grey-box li::before{content:"•";position:absolute;left:-16px;font-size:5px}
.photo{position:absolute}
</style>
</head>
<body>

<section class="page page-cover">
  <svg class="photo" style="left:0;top:0" width="334" height="240" viewBox="0 0 334 240" role="img" aria-label="Foto: Flusslandschaft mit Bäumen und Abendhimmel">
    <defs>
      <linearGradient id="river" x1="0" y1="0" x2="0" y2="1">
        <stop offset="0" stop-color="#dfe6ea"/>
        <stop offset="0.35" stop-color="#8fa0a8"/>
        <stop offset="0.55" stop-color="#3f4a3a"/>
        <stop offset="1" stop-color="#556b2a"/>
      </linearGradient>
    </defs>
    <path d="M0 0H334V230C250 205 150 205 70 170C40 158 15 165 0 172Z" fill="url(#river)"/>
    <path d="M0 172C15 165 40 158 70 170C150 205 250 205 334 230" fill="none" stroke="var(--blue)" stroke-width="3"/>
  </svg>
  <svg class="photo" style="left:16px;top:151px" width="68" height="68" viewBox="0 0 68 68" role="img" aria-label="Porträtfoto des Beraters">
    <circle cx="34" cy="34" r="32" fill="#d9c3b0" stroke="var(--blue)" stroke-width="3"/>
  </svg>
  <div class="brand">
    <div class="brand-address">Dr. Lukas T. Brenner<br>Am Lindenhang 8<br>CH-8004 Seewil<br>+41 70 555 20 40<br>lukas@brenner-rat.ch</div>
    <div class="brand-mark">lbr</div>
  </div>
  <h2 class="title abs" style="left:18px;top:241px;width:220px">Wann wird die Fahrt auf einem Fluss zum Genuss?</h2>
  <div class="abs" style="left:18px;top:288px;width:300px">
    <p>Eine Flussfahrt in einem Boot wird dann zum gelungenen Erlebnis, wenn von Anfang bis Ende alles passt. Dazu braucht es neben allgemeinem Grundwissen wie etwa über Wetterprognose oder Strömungsverhalten eine entsprechende Vorbereitung und eine gemeinsame Vorstellung über das Ziel einer Flussfahrt. Gibt es entlang der Route ein Wehr oder sonstige Hindernisse? Tückische Strömungsmuster? Wo sind die attraktiven Stellen zum Picknicken, ev. zum Baden? Wo sind mögliche Ausstiegsstellen? Und wie viele Personen sind am Boot? Wer macht was, damit alles koordiniert abläuft?</p>
    <p>Nun kann bei einer Bootsfahrt jeder einen Teil übernehmen, sich vorher informieren und sich dann einbringen. Oder sie können jemanden beauftragen, der weiss, worauf es ankommt und dem Unternehmen zum Erfolg verhilft.</p>
    <p>Mein Angebot ist es, Sie dabei zu unterstützen, den richtigen Weg mit ihrem Unternehmen, ihrer Organisation, ihrer Abteilung zu finden. Ihre Projekte also zum Fließen zu bringen.</p>
  </div>
  <h2 class="title abs" style="left:20px;top:409px;width:300px">Und was mache ich für Sie, damit Ihre Flussfahrt zum Erfolg wird?</h2>
</section>

<section class="page page-dynamics">
  <div class="brand">
    <div class="brand-address">Dr. Lukas T. Brenner<br>Am Lindenhang 8<br>CH-8004 Seewil<br>+41 70 555 20 40<br>lukas@brenner-rat.ch</div>
    <div class="brand-mark">lbr</div>
  </div>
  <h2 class="title abs" style="left:17px;top:28px">Umgebungsdynamik erfassen</h2>
  <p class="abs" style="left:18px;top:48px;width:204px">Unsere Gesellschaft wird immer komplexer und dynamischer. Es genügt nicht mehr, auf heutige Herausforderungen zu reagieren. Es müssen künftige Chancen und Potenziale frühzeitig erkannt und passende Antworten darauf gefunden werden. Gefragt sind massgeschneiderte, individuelle und kreative Lösungen mit möglichst bescheidenen Ressourcen.</p>
  <svg class="photo" style="left:228px;top:46px" width="106" height="51" role="img" aria-label="Foto: Meereswellen mit Gischt"><defs><linearGradient id="sea" x1="0" y1="0" x2="0" y2="1"><stop offset="0" stop-color="#2f6f8a"/><stop offset="0.5" stop-color="#bfe3ea"/><stop offset="1" stop-color="#1d4d6a"/></linearGradient></defs><rect width="106" height="51" fill="url(#sea)"/></svg>

  <h3 class="sub abs" style="left:19px;top:107px">Konkrete Angebote dazu:</h3>
  <svg class="abs" style="left:23px;top:132px" width="32" height="32" viewBox="0 0 32 32" aria-hidden="true">
    <circle cx="16" cy="16" r="15" fill="var(--olive)"/>
    <g fill="none" stroke="#6b6b4a" stroke-width="1.2"><circle cx="16" cy="8" r="2.5"/><circle cx="8" cy="21" r="2.5"/><circle cx="24" cy="21" r="2.5"/><path d="M16 11v6M16 17l-6 2M16 17l6 2"/></g>
  </svg>
  <div class="abs" style="left:57px;top:121px;width:265px">
    <p>Umfragen und Interviews mit Stakeholdern<br>Welche Bedürfnisse hat Ihr Umfeld hat bzw. wie nimmt es bestimmte Entwicklungen wahr? Wie nehmen Kunden, Mitarbeitende oder Mitglieder Ihre Organisation wahr?</p>
    <p>Ich unterstütze Sie durch die Planung und Realisierung von Umfragen, Interviews oder indem ich für Sie eine Internetrecherche durchführe. Ich liefere Ihnen die Ergebnisse, in Form von Fakten und Ideeninputs und diskutiere mit Ihnen mögliche Verwertungs- und Umsetzungsmassnahmen.</p>
  </div>

  <h3 class="sub abs" style="left:19px;top:196px">Internetrecherchen &amp; Studien</h3>
  <svg class="abs" style="left:24px;top:220px" width="26" height="22" viewBox="0 0 26 22" aria-hidden="true">
    <path d="M2 1v19h23" fill="none" stroke="#777" stroke-width="1"/>
    <path d="M5 15l6-4 5 3 7-8" fill="none" stroke="#777" stroke-width="0.8"/>
    <circle cx="5" cy="15" r="1.6" fill="var(--coral)"/><circle cx="11" cy="11" r="1.6" fill="var(--olive)"/><circle cx="16" cy="14" r="1.6" fill="var(--coral)"/><circle cx="23" cy="6" r="1.6" fill="var(--olive)"/>
  </svg>
  <div class="abs" style="left:57px;top:209px;width:265px">
    <p>Gibt es Themen, wie z.B. neue Geschäftsmodelle, neue Dienstleistungen, neue Mitwerber, über die sie gerne mehr Informationen hätten. Suchen Sie Wissen und Grundlagen für mögliche neue Wege, Strategien, Projekte? Das möglichst schnell, ohne viel Zeit zu investieren?</p>
    <p>Ich gestalte Ihnen ein mögliches Forschungsdesign und liefere Ihnen die Ergebnisse (ob in Form einer Präsentation, eines Berichts mit vorgeschlagenen Massnahmen oder als Zahlenwerk. Abgestimmt auf ihre Bedürfnisse</p>
  </div>

  <h2 class="title abs" style="left:20px;top:269px">Perspektiven schaffen</h2>
  <div class="grey-box abs" style="left:16px;top:291px;width:243px;height:59px">
    <ul>
      <li>Über den Tellerrand blicken und Neues entdecken</li>
      <li>Mögliche strategische Optionen oder operative Verbesserungsmassnahmen</li>
      <li>Visionen, Strategien, Ziele oder Projekte formulieren und den Weg dahin definieren</li>
      <li>Gefahren erkennen und mögliche Sicherheitsmassnahmen analysieren, bewerten und bestimmen</li>
    </ul>
  </div>
  <svg class="photo" style="left:265px;top:287px" width="69" height="66" role="img" aria-label="Foto: Brille vor unscharfer Stadtkulisse"><defs><linearGradient id="lens" x1="0" y1="0" x2="1" y2="1"><stop offset="0" stop-color="#7fa6b5"/><stop offset="0.6" stop-color="#2c4f66"/><stop offset="1" stop-color="#1a2a3a"/></linearGradient></defs><rect width="69" height="66" fill="url(#lens)"/></svg>
  <p class="abs" style="left:40px;top:350px;font-weight:700;color:var(--blue)">Not for Profit - Inhalte verfolgen und doch betriebswirtschaftlich agieren.</p>

  <h3 class="sub abs" style="left:19px;top:372px">Konkrete Angebote dazu:</h3>
  <div class="label abs" style="left:19px;top:384px">Projektplan mit konkreten Massnahmen entwerfen</div>
  <svg class="abs" style="left:18px;top:400px" width="26" height="26" viewBox="0 0 26 26" aria-hidden="true">
    <rect x="1" y="1" width="24" height="24" fill="#fff" stroke="#777"/>
    <path d="M3 23V9l14 14Z" fill="var(--olive)" stroke="#777" stroke-width="0.6"/>
    <path d="M9 3l14 14-2 2L7 5Z" fill="var(--coral)" stroke="#777" stroke-width="0.6"/>
  </svg>
  <div class="abs" style="left:53px;top:399px;width:268px">
    <p>Sie sollten eine Strategie entwickeln und auch formulieren, oder eine Jahresplanung und Ziele definieren? Projekte auf die Beine stellen oder für bestimmte Vorgaben konkrete Ziele formulieren?</p>
    <p>Ich plane und organisiere Strategieworkshops und moderiere diese als Aussenstehender. Ich plane und berechne mit Ihnen die Projektepläne und unterstütze Sie, dass diese dann auch realisiert werden.</p>
  </div>
</section>

<section class="page page-development">
  <div class="brand">
    <div class="brand-address">Dr. Lukas T. Brenner<br>Am Lindenhang 8<br>CH-8004 Seewil<br>+41 70 555 20 40<br>lukas@brenner-rat.ch</div>
    <div class="brand-mark">lbr</div>
  </div>
  <div class="label abs" style="left:19px;top:30px">Neue Wege der Kommunikation gestalten</div>
  <svg class="abs" style="left:22px;top:51px" width="36" height="32" viewBox="0 0 36 32" aria-hidden="true">
    <rect x="1" y="1" width="15" height="28" rx="2" fill="#9a9a9a"/><rect x="3" y="5" width="11" height="18" fill="var(--olive)"/>
    <rect x="19" y="1" width="15" height="28" rx="2" fill="#9a9a9a"/><rect x="21" y="5" width="11" height="18" fill="var(--coral)"/>
    <text x="8.5" y="18" font-family="Fira Sans,sans-serif" font-size="8" fill="#fff" text-anchor="middle">A</text>
    <text x="26.5" y="18" font-family="Fira Sans,sans-serif" font-size="8" fill="#fff" text-anchor="middle">B</text>
  </svg>
  <div class="abs" style="left:66px;top:44px;width:258px">
    <p>Sie haben Ihre eigene Kommunikationsagentur, die für Sie die konkrete Medienplanung betreibt, aber Sie wollen Ihre Kommunikation strategisch neu gestalten? Neue Medien, Ihren Webauftritt oder neue Zielgruppen ansprechen?</p>
    <p>Ich entwickle mit Ihnen entsprechende Kommunikationsstrategien oder auch ein konkretes Kommunikationsdesign (wie und wann kommunizieren wir mit wem?).</p>
  </div>

  <h2 class="title abs" style="left:18px;top:105px">Entwicklungen realisieren</h2>
  <p class="abs" style="left:19px;top:124px;width:300px;font-size:6.6px;line-height:8.6px">Sie haben Strategien, Ziele, sonstige Vorgaben und müssen diese neben Ihrem Alltagsgeschäft umsetzten. Dafür suchen Sie Unterstützung eines</p>
  <div class="grey-box abs" style="left:14px;top:146px;width:250px;height:96px;padding-left:24px">
    <ul>
      <li>Sparringpartners, mit dem Sie sich zu allgemeinen Herausforderungen oder konkreten Problemen austauschen wollen</li>
      <li>Moderators, der einen Strategieworkshop organisiert und auch dokumentiert</li>
      <li>Innovationsmanagers, der von aussen frischen Wind reinbringt</li>
      <li>Beraters mit der Kundenbrille, der die Kundensicht oder das Umfeld erforscht und hilft, neue Blickwinkel aber auch neue Lösungen hierfür zu entwickeln</li>
      <li>Kommunikators, der mit Stakeholdern in Kontakt tritt, bestehende Netzwerke nutzt und neue Netzwerke schafft</li>
      <li>erfahrenen Geschäftsführers, der hilft die Geschäftsstelle weiter zu professionalisieren und Finanzierungskonzepte zu entwickeln (inkl. Fundraising, Sponsoring und Crowdfunding)</li>
    </ul>
  </div>
  <svg class="photo" style="left:268px;top:165px" width="65" height="43" role="img" aria-label="Foto: Maschendrahtzaun vor orangem Hintergrund"><defs><linearGradient id="fence" x1="0" y1="0" x2="1" y2="1"><stop offset="0" stop-color="#4f8f9c"/><stop offset="0.5" stop-color="#c98a6e"/><stop offset="1" stop-color="#d9845f"/></linearGradient></defs><rect width="65" height="43" fill="url(#fence)"/></svg>

  <h3 class="sub abs" style="left:19px;top:247px">Konkrete Angebote dazu:</h3>
  <div class="label abs" style="left:19px;top:259px">Finanzierungskonzepte und konkrete Finanzierung</div>
  <svg class="abs" style="left:20px;top:278px" width="34" height="34" viewBox="0 0 34 34" aria-hidden="true">
    <circle cx="17" cy="17" r="16" fill="var(--olive)" stroke="#777"/>
    <path d="M5 19a12 12 0 0 1 24 0Z" fill="#fff" stroke="#777" stroke-width="0.8"/>
    <path d="M17 19l6-7" stroke="var(--coral)" stroke-width="1.6"/>
    <rect x="11" y="23" width="12" height="4" fill="#fff" stroke="#777" stroke-width="0.6"/>
  </svg>
  <div class="abs" style="left:65px;top:277px;width:262px">
    <p>Sie haben viele Projektideen, aber wenig finanzielle Mittel, um diese umzusetzen? Wo und wie kommen Sie zu diesen?</p>
    <p>Ich zeige Ihnen die verschiedenen Möglichkeiten einer Finanzierung auf und unterstütze bei der Realisierung (Fundraising generell, Sponsoring, Crowdfunding, etc.).</p>
  </div>

  <div class="label abs" style="left:19px;top:326px">Professionalisierung von BackOffice und Geschäftsstellen</div>
  <svg class="abs" style="left:21px;top:343px" width="30" height="30" viewBox="0 0 30 30" aria-hidden="true">
    <g stroke="#777" stroke-width="0.8" fill="none"><path d="M15 8v8M4 16h22M4 16v6M15 16v6M26 16v6"/></g>
    <rect x="11" y="1" width="8" height="7" fill="#aaa" stroke="#777" stroke-width="0.6"/>
    <rect x="1" y="22" width="6" height="6" fill="var(--coral)" stroke="#777" stroke-width="0.6"/>
    <rect x="12" y="22" width="6" height="6" fill="var(--olive)" stroke="#777" stroke-width="0.6"/>
    <rect x="23" y="22" width="6" height="6" fill="#e6b34a" stroke="#777" stroke-width="0.6"/>
  </svg>
  <div class="abs" style="left:64px;top:341px;width:262px">
    <p>Sie wollen die Administration, die Geschäftsprozesse, die ganze Geschäftsstelle optimieren?. Ob Technik, IT oder CRM oder noch konkreter: Geschäftsreglement, Handbuch, etc.</p>
    <p>Ich helfe Ihnen in der Analyse, in der Zielsetzung und -findung. Auch im Finden passender Experten.</p>
  </div>

  <div class="label abs" style="left:19px;top:396px">VR Mandate und Interimsmanagement</div>
  <svg class="abs" style="left:22px;top:408px" width="30" height="36" viewBox="0 0 30 36" aria-hidden="true">
    <path d="M15 35C6 24 1 19 1 14a14 14 0 0 1 28 0c0 5-5 10-14 21Z" fill="var(--olive)" stroke="#777"/>
    <circle cx="15" cy="14" r="9" fill="#fff" stroke="#777" stroke-width="0.8"/>
    <circle cx="15" cy="12" r="2.8" fill="none" stroke="#777" stroke-width="0.9"/>
    <path d="M10 19a5 4 0 0 1 10 0Z" fill="none" stroke="#777" stroke-width="0.9"/>
  </svg>
  <div class="abs" style="left:64px;top:410px;width:262px">
    <p>Sie suchen nach einem Experten, der in Ihrer Organisation für einen Übergangszeitraum die Geschäftsführung übernimmt? Oder Sie suchen ein Verwaltungsratsmitglied, das mit seinem Fachwissen Ihren Verwaltungsrat unterstützt?</p>
    <p>Nach Absprache kann ich eine VR- oder eine befristete GF Funktion übernehmen.</p>
  </div>
</section>

<section class="page page-profile">
  <div class="brand">
    <div class="brand-address">Dr. Lukas T. Brenner<br>Am Lindenhang 8<br>CH-8004 Seewil<br>+41 70 555 20 40<br>lukas@brenner-rat.ch</div>
    <div class="brand-mark">lbr</div>
  </div>
  <h2 class="title abs" style="left:18px;top:48px">Wofür stehe ich?</h2>
  <p class="abs" style="left:18px;top:80px;width:300px">Als Einzelperson stehe ich mit meiner Erfahrung, meinem Wissen und meiner Glaubwürdigkeit für Sie ein. Mein Zugang ist ein vernetzter und interdisziplinär. Ob nur in einem der oben angeführten Bereiche, oder in mehreren. Gerne unterstütze ich Sie.</p>
  <div class="abs" style="left:18px;top:110px;font-family:'Fira Sans',sans-serif;font-weight:500;font-size:7.6px;color:#444">lbr – das Optimum machen … mit Erfahrung und Methoden Knowhow</div>
  <p class="abs" style="left:18px;top:132px">Persönlich. Zuverlässig. Direkt. Individuell. Diskret.<br>Ich verspreche nicht zu viel, das aber halte ich.</p>
  <p class="abs" style="left:18px;top:156px;width:300px">Ich bringe langjährige Erfahrung als Geschäftsführer<br>kleinerer Unternehmen oder Organisationen ein (z.B. Forschungs- und<br>Beratungsunternehmen, Verband). Ebenso als<br>Bereichsleiter Corporate Development grosser Unternehmen<br>bis hin zu globalen Konzernen. In der profitorientierten wie<br>auch in der Non Profit Wirtschaft.<br>Meine ausgewiesenen Kompetenzen liegen in der Methodenkompetenz bei Strategie- und Organisationsentwicklung, in der Kommunikation sowie im Wissens- und Innovationsmanagement</p>
  <svg class="photo" style="left:96px;top:246px" width="96" height="96" viewBox="0 0 96 96" role="img" aria-label="Porträtfoto des Beraters">
    <circle cx="48" cy="48" r="45" fill="#dcc7b4" stroke="var(--blue)" stroke-width="4"/>
  </svg>
  <svg class="abs" style="left:0;top:320px" width="334" height="152" viewBox="0 0 334 152" aria-hidden="true">
    <path d="M0 60C90 45 200 40 270 25C300 18 320 12 334 8V152H0Z" fill="var(--blue)"/>
  </svg>
  <div class="abs" style="left:30px;top:404px;width:202px;text-align:right;color:#fff;font-size:7.6px;line-height:9.6px">
    Dr. Lukas T. Brenner&nbsp;&nbsp; Am Lindenhang 8&nbsp;&nbsp; CH-8004 Seewil<br>+41 70 555 20 40&nbsp;&nbsp;&nbsp; lukas@brenner-rat.ch
  </div>
  <div class="brand-mark abs" style="left:244px;top:396px;width:34px;height:34px;font-size:13px">lbr</div>
</section>

</body>
</html>
```